Commercial Construction Company

We need a business card design based on our current logo. We are a commercial general contractor based in Southern California that specializes in bank remodels. We would like to see designs that incorporate dark blue. The final design should portray an image of professionalism and quality.

If possible, I would like to add metallic foil to the design. Thank you

```html
<!DOCTYPE html>
<html lang="en">
<head>
<meta charset="utf-8">
<title>Halvard Construction Services – Business Card</title>
<link rel="stylesheet" href="https://fonts.googleapis.com/css2?family=Open+Sans:wght@400;600&family=Oswald:wght@500&display=swap">
<style>
  :root {
    --backdrop: #f34b4b;
    --navy: #1b1c55;
    --navy-deep: #14153f;
    --gold: #c9a45c;
    --gold-soft: #d8bb7c;
  }
  * { margin: 0; padding: 0; box-sizing: border-box; }
  html, body { width: 1200px; height: 1071px; overflow: hidden; }
  body {
    background: var(--backdrop);
    display: flex;
    flex-direction: column;
    align-items: center;
    justify-content: center;
    gap: 60px;
    font-family: "Open Sans", Arial, sans-serif;
    color: var(--gold);
  }
  .card {
    position: relative;
    width: 560px;
    height: 320px;
    background: radial-gradient(ellipse at 40% 40%, var(--navy) 0%, var(--navy-deep) 100%);
    box-shadow: 0 18px 40px rgba(90, 0, 0, 0.35);
    overflow: hidden;
  }
  .card__texture {
    position: absolute;
    inset: 0;
    background: linear-gradient(135deg, rgba(255,255,255,0.03), rgba(0,0,0,0.06));
  }
  .brand {
    position: absolute;
    display: flex;
    align-items: center;
    gap: 10px;
  }
  .brand__dot {
    width: 18px; height: 18px;
    border-radius: 50%;
    background: var(--gold);
  }
  .brand__name {
    font-family: "Open Sans", Arial, sans-serif;
    font-weight: 600;
    color: var(--gold);
    letter-spacing: 0.04em;
  }
  .card--front .brand {
    left: 50%; top: 50%;
    transform: translate(-50%, -50%);
  }
  .card--front .brand__name { font-size: 30px; }
  .card--back .brand {
    left: 36px; top: 50%;
    transform: translateY(-50%);
  }
  .card--back .brand__name { font-size: 22px; }
  .divider {
    position: absolute;
    left: 212px; top: 78px;
    width: 1px; height: 166px;
    background: var(--gold);
  }
  .details {
    position: absolute;
    left: 240px; top: 60px;
    right: 24px;
  }
  .person__name {
    font-family: "Oswald", "Arial Narrow", sans-serif;
    font-weight: 500;
    font-size: 25px;
    letter-spacing: 0.01em;
    text-transform: uppercase;
    line-height: 1.1;
  }
  .person__title {
    font-size: 11.5px;
    color: var(--gold-soft);
    margin-top: 2px;
  }
  .contact {
    display: flex;
    align-items: center;
    gap: 14px;
    margin-top: 16px;
    font-size: 11.5px;
    line-height: 1.45;
  }
  .contact__rule {
    width: 1px; height: 30px;
    background: var(--gold);
  }
  .company {
    margin-top: 18px;
  }
  .company__name {
    font-size: 13px;
    font-weight: 600;
    letter-spacing: 0.28em;
    text-transform: uppercase;
  }
  .company__address {
    font-size: 11px;
    margin-top: 3px;
  }
</style>
</head>
<body>

  <section class="card card--front" aria-label="Card front">
    <div class="card__texture" role="img" aria-label="Subtle tonal navy paisley texture"></div>
    <div class="brand">
      <span class="brand__dot"></span>
      <span class="brand__name">HALVARD</span>
    </div>
  </section>

  <section class="card card--back" aria-label="Card back">
    <div class="card__texture" role="img" aria-label="Subtle tonal navy paisley texture"></div>
    <div class="brand">
      <span class="brand__dot"></span>
      <span class="brand__name">HALVARD</span>
    </div>
    <div class="divider"></div>
    <div class="details">
      <h1 class="person__name">Elias Brandt</h1>
      <p class="person__title">General Director</p>
      <div class="contact">
        <div class="contact__phones">
          <p>555 21 40 18</p>
          <p>555 63 92 07</p>
        </div>
        <span class="contact__rule"></span>
        <div class="contact__online">
          <p>www.halvardbuild.com</p>
          <p>info@halvardbuild.com</p>
        </div>
      </div>
      <div class="company">
        <p class="company__name">Halvard Construction Services</p>
        <p class="company__address">West 18th Avenue, 9th Floor, Lakeview, CA 900, USA</p>
      </div>
    </div>
  </section>

</body>
</html>
```